Gardener needs an exciting new flyer design.

I'm a passionate gardener that requires a custom flyer design for a owner operator gardening business. Design will be for a DL flyer. I'm based on the Sunshine coast in Queensland Australia. My target audience is the residential market on the Sunshine coast. Business name is Marlowe Greens. My services are, lawn mowing, weeding, Eco Friendly fertilizing, green waste removal, Mulching, tree and shrub pruning, Full garden makeovers, hedging, pressure cleaning, privacy screening, Timber deck rejuvenation, Planting, Turf preparation and installation, and much more. Free no obligation quotes, reliable and friendly service, great rates. 12 years experience. Web www.marlowegreens.com.au - Phone 0418527064 - Email doug@marlowegreens.com.au I would like the design to portray a friendly and professional approach.

Target Market(s)

Residential

Industry/Entity Type

Gardener

Font styles to use
Serif

Colors
9ccb3b
abd037
3176b5

Requirements
Must have
• my services, my logo, my contact details,

```html
<!DOCTYPE html>
<html lang="en">
<head>
<meta charset="utf-8">
<title>Marlowe Greens – DL Flyer</title>
<link rel="stylesheet" href="https://fonts.googleapis.com/css2?family=Cinzel:wght@400;600&family=Cinzel+Decorative:wght@700&family=Open+Sans:wght@400;700&display=swap">
<style>
  :root {
    --green: #9ccb3b;
    --green-light: #abd037;
    --green-dark: #4f9a2c;
    --blue: #3176b5;
    --navy: #1f3f8f;
    --white: #ffffff;
    --backdrop: #e6e7e9;
  }
  * { box-sizing: border-box; margin: 0; padding: 0; }
  html, body {
    width: 829px; height: 1200px; overflow: hidden;
    background: var(--backdrop);
  }
  .flyer {
    position: absolute; left: 154px; top: 10px;
    width: 520px; height: 1180px;
    background: var(--white);
    overflow: hidden;
  }
  .flyer__shapes { position: absolute; inset: 0; }
  .brand {
    position: absolute; top: 250px; left: 0; right: 0;
    display: flex; flex-direction: column; align-items: center; gap: 26px;
  }
  .brand__dot {
    width: 70px; height: 70px; border-radius: 50%;
    background: var(--green);
  }
  .brand__name {
    font-family: "Cinzel Decorative", serif; font-weight: 700;
    font-size: 40px; color: var(--green-dark); letter-spacing: 0.5px;
  }
  .services {
    position: absolute; top: 420px; left: 62px; right: 40px;
  }
  .services__title {
    font-family: "Cinzel", serif; font-weight: 600;
    font-size: 29px; color: var(--navy); margin-bottom: 10px;
  }
  .services__list { list-style: none; }
  .services__item {
    display: flex; align-items: flex-start; gap: 8px;
    font-family: "Open Sans", sans-serif; font-weight: 700;
    font-size: 20.5px; line-height: 26px; color: var(--navy);
  }
  .services__tick { flex: 0 0 18px; margin-top: 4px; }
  .services__item--more { padding-left: 26px; }
  .promises {
    position: absolute; top: 838px; left: 0; right: 0;
    text-align: center;
    font-family: "Cinzel", serif; font-weight: 400;
    font-size: 22px; line-height: 27px; color: var(--green-dark);
  }
  .contact {
    position: absolute; top: 1010px; left: 22px;
    font-family: "Open Sans", sans-serif; color: var(--white);
  }
  .contact__lead { font-size: 11px; margin-bottom: 14px; }
  .contact__line { font-size: 17px; line-height: 24px; }
</style>
</head>
<body>
<main class="flyer">
  <svg class="flyer__shapes" width="520" height="1180" viewBox="0 0 520 1180" aria-hidden="true">
    <path d="M0 0 H390 Q190 55 0 175 Z" fill="var(--green)"/>
    <path d="M0 175 Q190 55 390 0 H440 Q200 85 0 215 Z" fill="var(--navy)"/>
    <path d="M0 985 Q260 970 520 1005 V1180 H0 Z" fill="var(--navy)"/>
    <path d="M520 1030 V1180 H330 Z" fill="var(--green-light)"/>
    <path d="M520 1080 V1180 H420 Z" fill="var(--green)"/>
  </svg>

  <header class="brand">
    <span class="brand__dot"></span>
    <h1 class="brand__name">Marlowe Greens</h1>
  </header>

  <section class="services">
    <h2 class="services__title">Our Service Offered</h2>
    <ul class="services__list">
      <li class="services__item"><svg class="services__tick" width="18" height="18" viewBox="0 0 18 18"><path d="M2 10 L7 15 L16 2" stroke="var(--green)" stroke-width="4" fill="none" stroke-linecap="round"/></svg>Lawn mowing</li>
      <li class="services__item"><svg class="services__tick" width="18" height="18" viewBox="0 0 18 18"><path d="M2 10 L7 15 L16 2" stroke="var(--green)" stroke-width="4" fill="none" stroke-linecap="round"/></svg>Weeding</li>
      <li class="services__item"><svg class="services__tick" width="18" height="18" viewBox="0 0 18 18"><path d="M2 10 L7 15 L16 2" stroke="var(--green)" stroke-width="4" fill="none" stroke-linecap="round"/></svg>Eco Friendly fertilizing</li>
      <li class="services__item"><svg class="services__tick" width="18" height="18" viewBox="0 0 18 18"><path d="M2 10 L7 15 L16 2" stroke="var(--green)" stroke-width="4" fill="none" stroke-linecap="round"/></svg>Green waste removal</li>
      <li class="services__item"><svg class="services__tick" width="18" height="18" viewBox="0 0 18 18"><path d="M2 10 L7 15 L16 2" stroke="var(--green)" stroke-width="4" fill="none" stroke-linecap="round"/></svg>Mulching</li>
      <li class="services__item"><svg class="services__tick" width="18" height="18" viewBox="0 0 18 18"><path d="M2 10 L7 15 L16 2" stroke="var(--green)" stroke-width="4" fill="none" stroke-linecap="round"/></svg>Tree and shrub pruning</li>
      <li class="services__item"><svg class="services__tick" width="18" height="18" viewBox="0 0 18 18"><path d="M2 10 L7 15 L16 2" stroke="var(--green)" stroke-width="4" fill="none" stroke-linecap="round"/></svg>Full garden makeovers</li>
      <li class="services__item"><svg class="services__tick" width="18" height="18" viewBox="0 0 18 18"><path d="M2 10 L7 15 L16 2" stroke="var(--green)" stroke-width="4" fill="none" stroke-linecap="round"/></svg>Hedging</li>
      <li class="services__item"><svg class="services__tick" width="18" height="18" viewBox="0 0 18 18"><path d="M2 10 L7 15 L16 2" stroke="var(--green)" stroke-width="4" fill="none" stroke-linecap="round"/></svg>Pressure cleaning</li>
      <li class="services__item"><svg class="services__tick" width="18" height="18" viewBox="0 0 18 18"><path d="M2 10 L7 15 L16 2" stroke="var(--green)" stroke-width="4" fill="none" stroke-linecap="round"/></svg>Privacy screening</li>
      <li class="services__item"><svg class="services__tick" width="18" height="18" viewBox="0 0 18 18"><path d="M2 10 L7 15 L16 2" stroke="var(--green)" stroke-width="4" fill="none" stroke-linecap="round"/></svg>Timber deck rejuvenation</li>
      <li class="services__item"><svg class="services__tick" width="18" height="18" viewBox="0 0 18 18"><path d="M2 10 L7 15 L16 2" stroke="var(--green)" stroke-width="4" fill="none" stroke-linecap="round"/></svg>Planting</li>
      <li class="services__item"><svg class="services__tick" width="18" height="18" viewBox="0 0 18 18"><path d="M2 10 L7 15 L16 2" stroke="var(--green)" stroke-width="4" fill="none" stroke-linecap="round"/></svg>Turf preparation and installation</li>
      <li class="services__item services__item--more">and much more.</li>
    </ul>
  </section>

  <section class="promises">
    <p>Free No Obligation Quotes</p>
    <p>Reliable and Friendly Service</p>
    <p>Great Rates</p>
    <p>2 Years Experience</p>
  </section>

  <footer class="contact">
    <p class="contact__lead">For more details contact us on:</p>
    <p class="contact__line">Web : www.marlowegreens.com.au</p>
    <p class="contact__line">Phone : 0418527064</p>
    <p class="contact__line">Email : doug@marlowegreens.com.au</p>
  </footer>
</main>
</body>
</html>
```